Business Card Designs

Looking to design a 3.5" x 2" standard business card for our employees.
The design needs to be sleek, simple, and modern. We would like our logo (attached) to be incorporated, but not in that colour, rather an outline of the logo in either gold or silver (whichever looks better).

Modern and Simple is what we are looking for, but be creative in incorporating the logo.

```html
<!DOCTYPE html>
<html lang="en">
<head>
<meta charset="UTF-8">
<title>Harbourline Suites – Business Card</title>
<link href="https://fonts.googleapis.com/css2?family=Poppins:wght@400;600;700&display=swap" rel="stylesheet">
<style>
  :root{
    --stage:#2b2725;
    --card:#1c1c1c;
    --yellow:#ffd42a;
    --amber:#f7a707;
    --text:#e9e9e9;
  }
  *{box-sizing:border-box;margin:0;padding:0}
  html,body{width:1200px;height:842px;overflow:hidden;background:var(--stage)}
  body{position:relative;font-family:'Poppins',sans-serif}
  .card{position:absolute;width:540px;height:309px;background:var(--card);overflow:hidden;box-shadow:0 14px 30px rgba(0,0,0,.45)}
  .card--back{left:40px;top:266px}
  .card--front{left:620px;top:266px}

  /* back side */
  .band{position:absolute;left:0;width:100%;height:12px;background:var(--yellow)}
  .band--top{top:0}
  .band--bottom{bottom:16px}
  .details{position:absolute;left:0;right:0;top:58px;text-align:center;color:var(--text);text-transform:uppercase}
  .details__name{font-weight:700;font-size:21px;color:var(--yellow);letter-spacing:-.2px;line-height:1.1}
  .details__role{font-size:12.5px;letter-spacing:.5px;margin-top:2px}
  .divider{width:52px;height:2px;background:var(--amber);margin:10px auto}
  .details__line{font-size:12.5px;line-height:1.35;letter-spacing:.3px}
  .details__line--phone{font-size:15px}

  /* front side */
  .edge-mark{position:absolute;top:120px;height:70px}
  .edge-mark__block{position:absolute;top:0;width:46px;height:100%;background:var(--yellow)}
  .edge-mark__stripe{position:absolute;top:0;width:4px;height:100%;background:var(--amber)}
  .edge-mark--left{left:0;width:64px}
  .edge-mark--left .edge-mark__block{left:0}
  .edge-mark--left .edge-mark__stripe{left:52px}
  .edge-mark--right{right:0;width:64px}
  .edge-mark--right .edge-mark__block{right:0}
  .edge-mark--right .edge-mark__stripe{right:52px}
  .brand{position:absolute;left:0;right:0;top:0;bottom:0;display:flex;align-items:center;justify-content:center;gap:12px}
  .brand__square{width:16px;height:16px;background:var(--yellow)}
  .brand__name{font-weight:600;font-size:22px;letter-spacing:3px;color:var(--yellow);text-transform:uppercase}
</style>
</head>
<body>
  <section class="card card--back" aria-label="Card back with contact details">
    <div class="band band--top"></div>
    <div class="details">
      <p class="details__name">Daniel Reyes</p>
      <p class="details__role">Managing Director</p>
      <div class="divider"></div>
      <p class="details__line details__line--phone">055-987 654 321</p>
      <p class="details__line">hello@harbourline.com</p>
      <p class="details__line">www.harbourline.com</p>
      <div class="divider"></div>
      <p class="details__line">421, Address line goes here</p>
      <p class="details__line">45452, Country name</p>
    </div>
    <div class="band band--bottom"></div>
  </section>

  <section class="card card--front" aria-label="Card front with company name">
    <div class="edge-mark edge-mark--left"><span class="edge-mark__block"></span><span class="edge-mark__stripe"></span></div>
    <div class="brand">
      <span class="brand__square"></span>
      <span class="brand__name">Harbourline Suites</span>
    </div>
    <div class="edge-mark edge-mark--right"><span class="edge-mark__block"></span><span class="edge-mark__stripe"></span></div>
  </section>
</body>
</html>
```